Mirabotta war genau die Richtige für mich. Sie hat zügig und professionell gearbeitet und ihr Entwurf hat genau meinen Geschmack getroffen. Die Kommunikation war sehr freundlich und klar.
Zielgruppe
Ich bin Systemische Coach und möchte eine Methode bewerben. Es geht dabei um Auflösung von Schocktraumata. Also Trauma nach Unfall, Gewalterfahrung, Katastrophe, Diagnose, Operation, traumatischer Geburt, etc.
Mein Flyer soll Menschen erreichen, die so etwas erlebt haben und bei denen das Ereignis immer noch getriggert wird. z.B. Polizist:innen, Rettungshelfer:innen, Ärzt:innen
Genaueres hier: www.ruhe-anker.de
Die Methode bietet schnelle Hilfe, arbeitet mit Visualisierung und Klopfen, und retraumatisiert nicht.
Aufgabenstellung
Design sollte sich an der Website orientieren. Texte können davon genommen werden.
Anbei noch ein Text, der in einem Veranstaltungsnewsletter erscheint.
Bildmaterial ebenfalls von Website (bitte dann anfragen, was gebraucht wird) oder sehr gerne auch anderes von bilder.kavomex.com
Format: Din lang, 4 Seiten, hoch oder quer ist egal

```html
<!DOCTYPE html>
<html lang="de">
<head>
<meta charset="utf-8">
<title>Anker Release Technique – Flyer DIN lang</title>
<link rel="stylesheet" href="https://fonts.googleapis.com/css2?family=Open+Sans:ital,wght@0,400;0,600;0,700;1,400&family=Itim&display=swap">
<style>
:root{
  --ink:#2b2b33;
  --title:#3e3f9c;
  --band:#7f7fbf;
  --band-dark:#4a4d9e;
  --lilac:#d5d3ef;
  --lilac-soft:#e6e4f6;
  --paper:#ffffff;
  --grey-top:#f1f1f4;
  --grey-bottom:#d3d3d8;
  --backdrop:#e9e9ec;
}
*{box-sizing:border-box;margin:0;padding:0}
html,body{width:860px;height:1200px;overflow:hidden}
body{background:var(--backdrop);font-family:"Open Sans",Arial,sans-serif;color:var(--ink);position:relative}
.sheet{position:absolute;left:20px;width:820px;height:575px;background:var(--paper);box-shadow:0 3px 10px rgba(0,0,0,.12);overflow:hidden}
.sheet--outside{top:12px}
.sheet--inside{top:613px}
.panel{position:absolute;top:0;width:273.33px;height:100%;overflow:hidden}
.panel--a{left:0}.panel--b{left:273.33px}.panel--c{left:546.66px}
.footer-band{position:absolute;left:0;right:0;bottom:0;height:30px;background:var(--band-dark);color:#fff;font-weight:700;font-size:12.5px;display:flex;align-items:center;justify-content:center}
.hand{font-family:"Itim",cursive}
.photo{position:absolute}

/* outside: panel 5 */
.intro{position:absolute;top:52px;left:0;right:0;text-align:center}
.intro h2{color:var(--title);font-size:10.5px;font-weight:700;line-height:1.3}
.intro p{font-size:8.5px;line-height:1.35;margin-top:6px}
.photo--flower{top:168px;left:0;right:0;bottom:30px;background:linear-gradient(180deg,#f6d9a6 0%,#e9b57f 25%,#b49582 55%,#8c7b72 80%,#6e625c 100%)}
.photo--flower::before{content:"";position:absolute;top:0;left:0;right:0;height:3px;background:var(--band-dark)}
.quote{position:absolute;top:190px;left:34px;right:34px;text-align:center;color:var(--title);font-size:10.5px;line-height:1.45;font-style:italic}
.quote p+p{margin-top:8px}
.quote cite{display:block;text-align:right;font-family:"Open Sans",sans-serif;font-size:8.5px;font-style:normal}

/* outside: panel 6 */
.assure{position:absolute;top:48px;left:20px;right:20px;text-align:center;color:var(--title)}
.assure strong{display:block;font-size:10px;line-height:1.25;font-weight:700}
.assure .solution{display:block;font-size:16px;margin:14px 0 12px;font-weight:400}
.chance-band{position:absolute;top:205px;left:0;right:0;height:104px;background:var(--band)}
.chance-band h2{color:#fff;font-weight:400;font-size:22px;line-height:1.05;text-align:center;margin-top:14px;letter-spacing:.5px}
.contact{position:absolute;top:288px;left:32px;width:210px;height:222px;background:var(--lilac);text-align:center;color:var(--ink)}
.contact h3{color:var(--title);font-size:11px;font-weight:700;margin-top:10px}
.photo--portrait{left:31px;right:31px;top:32px;height:64px;background:linear-gradient(90deg,#5c5a5c 0%,#8e7d72 45%,#e7e6e2 100%)}
.contact .name{position:absolute;top:104px;left:0;right:0;color:var(--title);font-weight:700;font-size:9.5px}
.contact ul{list-style:none;position:absolute;top:122px;left:32px;text-align:left;font-size:8.5px;line-height:1.5}
.contact li{display:flex;align-items:center;gap:5px}
.contact svg{width:9px;height:9px;fill:var(--band-dark)}
.contact .practice{position:absolute;top:168px;left:0;right:0;font-size:8.5px;line-height:1.45}
.contact .practice b{color:var(--title);font-size:9.5px;display:block;margin-bottom:1px}

/* outside: panel 1 */
.panel--cover{background:#fafafc}
.brand{position:absolute;top:32px;left:0;right:0;text-align:center}
.brand-dot{display:block;width:58px;height:58px;margin:0 auto 14px;border-radius:50%;background:var(--lilac)}
.brand-name{color:var(--title);font-size:18px}
.cover-band{position:absolute;top:208px;left:0;right:0;height:100px;background:var(--band);color:#fff;text-align:center}
.cover-band h2{font-size:11.5px;font-weight:600;line-height:1.35;margin-top:10px}
.cover-band p{font-size:9px;font-weight:600;line-height:1.35;margin-top:8px;padding:0 12px}
.photo--beach{top:308px;left:0;right:0;bottom:30px;background:linear-gradient(180deg,#c9cdd3 0%,#b5bcc3 30%,#8e9aa4 38%,#b8a48b 48%,#a99279 75%,#8f7a63 100%)}

/* inside */
.panel--intro{background:linear-gradient(180deg,var(--grey-top) 0%,var(--grey-bottom) 100%)}
.panel--symptoms{background:linear-gradient(180deg,#f6f6f8 0%,#e4e4e8 100%)}
.panel--unique{background:#fff}
.photo-frame{position:absolute;top:0;left:0;right:0;height:118px;background:var(--band-dark)}
.panel--symptoms .photo-frame{background:var(--band);height:120px}
.panel--unique .photo-frame{background:var(--lilac)}
.photo--session{top:12px;left:12px;right:12px;height:132px;background:linear-gradient(90deg,#e6d6b8 0%,#f0efe9 40%,#f6f6f4 60%,#8a7a74 85%,#d9d5cf 100%)}
.photo--session-2{background:linear-gradient(90deg,#e2cfb0 0%,#ecebe6 40%,#f4f4f2 58%,#7c6c66 82%,#dcd8d2 100%)}
.photo--session-3{background:linear-gradient(90deg,#ece3d2 0%,#f3eee4 35%,#e8e5de 55%,#7b6b63 78%,#e6e3dd 100%)}
.copy{position:absolute;top:166px;left:22px;right:22px;font-size:8.6px;line-height:1.3}
.copy h2{color:var(--title);font-size:11px;font-weight:700;margin-bottom:4px}
.copy p{margin-bottom:6px;text-align:justify;hyphens:auto}
.copy .lead{color:var(--title);font-weight:700}
.copy ul{list-style:none}
.copy li{position:relative;padding-left:8px;margin-bottom:3.5px}
.copy li::before{content:"";position:absolute;left:0;top:4.5px;width:3px;height:3px;border-radius:50%;background:var(--band-dark)}
.copy h2.second{margin-top:14px}
.copy b{font-weight:700}
.inside-band{position:absolute;left:0;right:0;bottom:0;height:30px;display:flex}
.inside-band span{flex:1}
</style>
</head>
<body>

<section class="sheet sheet--outside" aria-label="Außenseite">
  <article class="panel panel--a">
    <div class="intro">
      <h2>Haben Sie schon mal etwas erlebt, das tiefe<br>Spuren in Ihrer Psyche hinterlassen hat?</h2>
      <p>Unfall / Operation / Diagnose / Todesfall<br>Trennung / Scheidung / schlechte Nachrichten<br>Gewalt / Flucht / Versagen / Naturkatastrophe</p>
    </div>
    <div class="photo photo--flower" role="img" aria-label="Foto: rosa Blume wächst aus einem Riss im Asphalt im Abendlicht"></div>
    <blockquote class="quote hand">
      <p>Dass die Vögel der Sorge und des Kummers über deinem Haupt fliegen, kannst du nicht ändern.</p>
      <p>Doch du kannst verhindern, dass sie Nester in deinem Haar bauen.</p>
      <cite>(Volksweisheit)</cite>
    </blockquote>
    <div class="footer-band">www.ruhe-anker.de</div>
  </article>

  <article class="panel panel--b">
    <div class="assure">
      <strong>Sie müssen nicht mit schlimmen Erinnerungen leben und diese immer wieder durchleiden.</strong>
      <span class="solution hand">Es gibt eine Lösung!</span>
      <strong>In einem vertraulichen Gespräch klären wir die Möglichkeiten.</strong>
    </div>
    <div class="chance-band"><h2 class="hand">Geben Sie sich<br>eine Chance!</h2></div>
    <div class="contact">
      <h3>Kontakt:</h3>
      <div class="photo photo--portrait" role="img" aria-label="Porträtfoto der Coachin"></div>
      <div class="name">Mirela Santorin Vahlberg</div>
      <ul>
        <li><svg viewBox="0 0 24 24"><path d="M6.6 10.8a15.1 15.1 0 0 0 6.6 6.6l2.2-2.2a1 1 0 0 1 1-.25 11.4 11.4 0 0 0 3.6.57 1 1 0 0 1 1 1V20a1 1 0 0 1-1 1A17 17 0 0 1 3 4a1 1 0 0 1 1-1h3.5a1 1 0 0 1 1 1c0 1.25.2 2.45.57 3.57a1 1 0 0 1-.25 1z"/></svg>+49 (0)170 55 20 418</li>
        <li><svg viewBox="0 0 24 24"><path d="M2 5h20v14H2z M3 6l9 7 9-7" fill="none" stroke="#4a4d9e" stroke-width="2"/></svg>info@ruhe-anker.de</li>
        <li><svg viewBox="0 0 24 24"><g fill="none" stroke="#4a4d9e" stroke-width="2"><circle cx="12" cy="12" r="9"/><path d="M3 12h18M12 3c3 3 3 15 0 18M12 3c-3 3-3 15 0 18"/></g></svg>www.ruhe-anker.de</li>
      </ul>
      <p class="practice"><b>Praxis am Lindenhof</b>Ahornweg 14<br>79100 Talbrück</p>
    </div>
    <div class="footer-band">www.ruhe-anker.de</div>
  </article>

  <article class="panel panel--c panel--cover">
    <div class="brand">
      <span class="brand-dot"></span>
      <span class="brand-name hand">Anker Release Technique</span>
    </div>
    <div class="cover-band">
      <h2>Sie können Ihr<br>Schocktrauma auflösen!</h2>
      <p>Befreien Sie sich von den Nachwirkungen der Erfahrung und erleben Sie ein unbeschwerteres, freieres Sein.</p>
    </div>
    <div class="photo photo--beach" role="img" aria-label="Foto: Frau springt mit ausgebreiteten Armen am Strand zwischen auffliegenden Möwen"></div>
    <div class="footer-band">www.ruhe-anker.de</div>
  </article>
</section>

<section class="sheet sheet--inside" aria-label="Innenseite">
  <article class="panel panel--a panel--intro">
    <div class="photo-frame"></div>
    <div class="photo photo--session" role="img" aria-label="Foto: Coachin im Gespräch mit einer Klientin"></div>
    <div class="copy">
      <h2>Haben Sie ein Trauma?</h2>
      <p class="lead">Sie haben Schlimmes erlebt und es sitzt Ihnen noch in den Knochen, hängt Ihnen nach, holt Sie ein, triggert Sie…? Sie erleben Albträume, Flashbacks, fühlen sich blockiert, verletzt, gebremst, beschämt, schuldig, überschattet, wie im Nebel, zerbrochen…?</p>
      <p>Egal, wie „groß“ oder „klein“ die Verletzung (griechisch: Trauma) war, lassen Sie nicht zu, dass sie Ihr Leben bestimmt, Sie beeinträchtigt, Sie davon abhält, Dinge zu tun, die Sie gerne tun würden.</p>
      <p>Sie brauchen nicht darauf zu warten, dass „die Zeit alle Wunden heilt“… Sie können jetzt sofort etwas tun, um die Verbindung zwischen dem Ereignis und den Mustern zu entkoppeln, die automatisch im Gehirn und Körper gestartet werden, sobald Sie etwas daran erinnert, es also einen Auslöser oder Trigger gibt.</p>
      <p>Dies gelingt mit der Anwendung der Anker Release Technique – einer Methode, die durch eine Kombination aus Klopf-Akupressur und auditiv-visuellen-motorischen Reizen neuronale Veränderungen im Gehirn bewirkt. Neuronale Muster, die durch das Trauma entstanden sind, werden gelöst und neu konditioniert.</p>
      <p class="lead">Das Geschehene wird zu einer normalen Erinnerung und löst keine Symptome mehr aus.</p>
    </div>
    <div class="inside-band"><span style="background:#444893"></span><span style="background:#555897"></span></div>
  </article>

  <article class="panel panel--b panel--symptoms">
    <div class="photo-frame"></div>
    <div class="photo photo--session photo--session-2" role="img" aria-label="Foto: Klientin mit Hand auf der Brust während der Sitzung"></div>
    <div class="copy">
      <h2>Psychische Symptome von Trauma</h2>
      <ul>
        <li>Schock, Leugnung oder Unglauben</li>
        <li>Wut, Reizbarkeit, Stimmungsschwankungen</li>
        <li>Schuldgefühle, Scham, Selbstvorwürfe</li>
        <li>Gefühl der Traurigkeit, Hoffnungslosigkeit, Unbeteiligtheit oder Gefühllosigkeit</li>
        <li>Rückzug von anderen, obwohl die Isolation alles noch schlimmer macht.</li>
        <li>Verwirrung, Konzentrationsschwierigkeiten; klares Denken ist schwierig oder unmöglich; nebliger Geist</li>
        <li>Ängstlichkeit und Furcht</li>
        <li>Verzweiflung, Verlust des Selbstwertgefühls und häufig Depression</li>
        <li>Hypervigilanz – erhöhte wachsame Beobachtung des Geschehens um einen herum, die zu extremer Anspannung führt.</li>
      </ul>
      <h2 class="second">Körperliche Symptome von Trauma</h2>
      <p>Schlaflosigkeit oder Albträume, Schreckhaftigkeit, Herzrasen, Engegefühl in der Brust, Körperliche Schmerzen, Muskelverspannungen, Müdigkeit, Reizbarkeit, Gereiztheit, Unruhe, Ungeduld</p>
    </div>
    <div class="inside-band"><span style="background:#5d5fa3"></span><span style="background:#7676b4"></span></div>
  </article>

  <article class="panel panel--c panel--unique">
    <div class="photo-frame"></div>
    <div class="photo photo--session photo--session-3" role="img" aria-label="Foto: Coachin führt die Klopftechnik an der Stirn der Klientin aus"></div>
    <div class="copy">
      <h2>Was macht ART so einzigartig?</h2>
      <ul>
        <li>Der ART-Prozess ist <b>sehr sanft</b>. Eine Sitzung mit ART ist in der Regel wenig belastend, wodurch das Retraumatisierungsrisiko sehr gering ist.</li>
        <li>Die Technik ist so konzipiert, dass schon früh im Prozess <b>im sicheren Abstand vom Fühlen</b> gearbeitet wird. Hierdurch braucht es wenig stabilisierende Vorarbeit.</li>
        <li>ART ist ein relativ <b>schneller Prozess</b>. Die meisten Schocktraumata lassen sich im Rahmen einer Sitzung lösen.</li>
        <li>Die erleichternde <b>Wirkung</b> ist <b>sofort spürbar</b>.</li>
        <li>Basierend auf jahrelangen Erfahrungen von Lorena Walsby und vieler ART-Anwender/innen weltweit, wirkt eine genau nach dem Protokoll durchgeführte Sitzung <b>nachhaltig</b> und braucht in der Regel keine Folgesitzungen oder sonstige Nachbearbeitung.</li>
        <li>ART ist geeignet für <b>Erwachsene</b> und <b>Kinder</b> aller kultureller und religiöser Hintergründe.</li>
        <li>Die Technik kann auf <b>alle belastenden Erinnerungen</b>, die einen Schock- oder Schreckmoment enthalten, angewandt werden.</li>
        <li>Dabei ist es unerheblich, wie lange das Erlebte zurückliegt. <b>Es muss nur eine bewusste Erinnerung in Form von Gesehenem oder Gehörtem vorhanden sein.</b></li>
      </ul>
    </div>
    <div class="inside-band"><span style="background:#8686c2;flex:.3"></span><span style="background:var(--lilac)"></span></div>
  </article>
</section>

</body>
</html>
```